Cardiology practice business card

We need a business card for our cardiology practice "Bellmoor Cardiology". We have a new logo, attached below. We like the colours in the logo - red and charcoal. The front of the business card will need to have the doctors name, address, phone number and email. The back will need to have space to write 2 appointment dates and times.

```html
<!DOCTYPE html>
<html lang="en">
<head>
<meta charset="utf-8">
<title>Bellmoor Cardiology – Business Card</title>
<link href="https://fonts.googleapis.com/css2?family=Quicksand:wght@500;600;700&display=swap" rel="stylesheet">
<style>
  :root {
    --red: #d91c24;
    --charcoal: #3a3a3c;
    --ink: #222226;
    --grey-line: #6a6a6e;
    --card: #ffffff;
    --card-shade: #f1f1f1;
    --backdrop: #2b2b2d;
  }
  * { margin: 0; padding: 0; box-sizing: border-box; }
  html, body {
    width: 1200px; height: 900px; overflow: hidden;
    background: var(--backdrop);
    font-family: "Quicksand", sans-serif;
  }
  .canvas {
    position: relative; width: 1200px; height: 900px;
  }
  .card {
    position: absolute; left: 260px;
    width: 680px; height: 390px;
    background: linear-gradient(135deg, var(--card) 0%, var(--card) 55%, var(--card-shade) 100%);
    box-shadow: 0 12px 30px rgba(0,0,0,.45);
    overflow: hidden;
  }
  .card--back { top: 40px; }
  .card--front { top: 470px; }
  .card__band {
    position: absolute; left: 0; right: 0; bottom: 0; height: 24px;
    background: var(--red);
  }
  .brand {
    position: absolute; top: 48px; right: 48px;
    display: flex; align-items: center; gap: 10px;
    font-weight: 700; font-size: 30px; color: var(--red);
    letter-spacing: .5px;
  }
  .brand__dot {
    width: 16px; height: 16px; border-radius: 50%; background: var(--red);
  }

  /* Appointment side */
  .appointment__head {
    position: absolute; left: 48px; top: 190px; right: 48px;
    display: flex; align-items: flex-end; gap: 10px;
    color: var(--red); font-weight: 600; font-size: 19px;
  }
  .appointment__head::after {
    content: ""; flex: 1; border-bottom: 1px solid var(--red); margin-bottom: 6px;
  }
  .appointment__row {
    position: absolute; left: 48px; right: 48px;
    display: flex; align-items: flex-end; gap: 10px;
    color: var(--ink); font-weight: 500; font-size: 18px;
  }
  .appointment__row--one { top: 250px; }
  .appointment__row--two { top: 305px; }
  .appointment__fill {
    flex: 1; border-bottom: 1.5px dashed var(--ink); margin-bottom: 5px;
  }
  .appointment__fill--date { flex: 1.4; }

  /* Contact side */
  .doctor {
    position: absolute; left: 48px; top: 190px; right: 48px;
  }
  .doctor__name {
    font-size: 22px; font-weight: 600; color: var(--red);
  }
  .doctor__creds { color: var(--charcoal); font-weight: 500; font-size: 17px; }
  .doctor__role {
    display: flex; align-items: flex-end; gap: 12px; margin-top: 2px;
    font-size: 19px; font-weight: 600; color: var(--ink);
  }
  .doctor__role::after {
    content: ""; flex: 1; border-bottom: 1px solid var(--grey-line); margin-bottom: 6px;
  }
  .address {
    position: absolute; right: 48px; top: 262px;
    text-align: right; font-size: 16px; font-weight: 500;
    color: var(--charcoal); line-height: 1.45;
  }
  .contact {
    position: absolute; left: 78px; top: 290px;
    list-style: none; font-size: 17px; font-weight: 500; color: var(--charcoal);
  }
  .contact__item { display: flex; align-items: center; gap: 10px; height: 30px; }
  .contact__icon { width: 16px; height: 16px; fill: var(--red); flex: none; }
</style>
</head>
<body>
<main class="canvas">

  <section class="card card--back" aria-label="Appointment side">
    <div class="brand"><span class="brand__dot"></span>Bellmoor Cardiology</div>
    <p class="appointment__head">Your Appointment</p>
    <div class="appointment__row appointment__row--one">
      <span>Date</span><span class="appointment__fill appointment__fill--date"></span>
      <span>Time</span><span class="appointment__fill"></span>
    </div>
    <div class="appointment__row appointment__row--two">
      <span>Date</span><span class="appointment__fill appointment__fill--date"></span>
      <span>Time</span><span class="appointment__fill"></span>
    </div>
    <div class="card__band"></div>
  </section>

  <section class="card card--front" aria-label="Contact side">
    <div class="brand"><span class="brand__dot"></span>Bellmoor Cardiology</div>
    <div class="doctor">
      <p><span class="doctor__name">Dr Owen Hartley</span> <span class="doctor__creds">| MBBS, FRACP</span></p>
      <p class="doctor__role">Consultant Cardiologist &amp; Physician</p>
    </div>
    <ul class="contact">
      <li class="contact__item">
        <svg class="contact__icon" viewBox="0 0 24 24" aria-hidden="true"><path d="M6.6 10.8a15.1 15.1 0 0 0 6.6 6.6l2.2-2.2a1 1 0 0 1 1-.25 11.4 11.4 0 0 0 3.6.57 1 1 0 0 1 1 1V20a1 1 0 0 1-1 1A17 17 0 0 1 3 4a1 1 0 0 1 1-1h3.5a1 1 0 0 1 1 1c0 1.25.2 2.45.57 3.57a1 1 0 0 1-.25 1z"/></svg>
        (07) 4011 2845
      </li>
      <li class="contact__item">
        <svg class="contact__icon" viewBox="0 0 24 24" aria-hidden="true"><path d="M2 5h20v14H2zm2 2v.5l8 5 8-5V7zm0 2.8V17h16V9.8l-8 5z"/></svg>
        reception@bellmoorcardio.com.au
      </li>
    </ul>
    <p class="address">Level 2, Bellmoor Private Hospital<br>58 Harbour Road, Bellmoor QLD</p>
    <div class="card__band"></div>
  </section>

</main>
</body>
</html>
```